Quillbrook
Quillbrook - Construction
Professional
Dale
Partner
4821 Fennmoor Ave Charlotte, NC 28391
d_q7@zentramail.net
Harriet7 Harriet7
Please use the most current design. you may remove demolition and remediation but please keep the slogan
Can you change construction to Demolition & Remediation?

```html
<!DOCTYPE html>
<html lang="en">
<head>
<meta charset="utf-8">
<title>Quillbrook – Stationery Set</title>
<link rel="stylesheet" href="https://fonts.googleapis.com/css2?family=Titillium+Web:wght@400;700&display=swap">
<style>
  :root {
    --navy: #1b2236;
    --navy-light: #232b42;
    --green: #3fae49;
    --paper: #ffffff;
    --paper-shade: #eef0f2;
    --backdrop: #e9e4dc;
    --ink-soft: #7a7f88;
    --ink-on-dark: #c6cad4;
    --mark-faint: #d9dbde;
  }
  * { box-sizing: border-box; margin: 0; padding: 0; }
  html, body { width: 1200px; height: 638px; overflow: hidden; }
  body {
    position: relative;
    background: var(--backdrop);
    font-family: "Titillium Web", Arial, sans-serif;
    color: var(--navy);
  }
  .piece { position: absolute; background: var(--paper); box-shadow: 0 2px 6px rgba(0,0,0,.18); overflow: hidden; }

  .wordmark { font-weight: 700; color: var(--navy); letter-spacing: .5px; line-height: 1; white-space: nowrap; }
  .tagline { color: var(--green); font-size: 6px; letter-spacing: 1px; text-transform: uppercase; white-space: nowrap; }

  /* Presentation folder */
  .folder { left: 82px; top: 101px; width: 549px; height: 492px; }
  .folder-spine { position: absolute; left: 261px; top: 0; width: 1px; height: 100%; background: var(--paper-shade); }
  .folder-pockets { position: absolute; left: 0; top: 0; }
  .folder .cover-brand { position: absolute; left: 314px; top: 103px; }
  .folder .cover-brand .wordmark { font-size: 30px; }
  .folder .cover-brand .tagline { margin-top: 3px; }
  .folder .inside-brand { position: absolute; left: 110px; top: 318px; font-size: 10px; }
  .folder .pocket-note { position: absolute; left: 58px; top: 410px; font-size: 5px; color: #5d6578; white-space: nowrap; }

  .inserted-card { position: absolute; left: 350px; top: 381px; width: 132px; height: 76px; background: var(--navy-light); box-shadow: 0 1px 4px rgba(0,0,0,.35); overflow: hidden; }
  .inserted-card .white-face { position: absolute; inset: 0; background: var(--paper); clip-path: polygon(62% 0, 100% 0, 100% 100%, 44% 100%); }
  .inserted-card .name { position: absolute; left: 9px; top: 16px; color: var(--paper); font-size: 7px; font-weight: 700; }
  .inserted-card .lines { position: absolute; left: 9px; top: 28px; color: var(--ink-on-dark); font-size: 4.5px; line-height: 1.5; white-space: nowrap; }

  /* Letterhead */
  .letterhead { left: 641px; top: 101px; width: 204px; height: 348px; }
  .letterhead .head { position: absolute; left: 20px; top: 22px; }
  .letterhead .head .wordmark { font-size: 14px; }
  .letterhead .head .tagline { font-size: 3.5px; margin-top: 2px; }
  .letterhead .faint-block { position: absolute; left: 67px; top: 120px; width: 70px; height: 70px; background: var(--mark-faint); }
  .letterhead .footer { position: absolute; left: 20px; top: 280px; font-size: 4px; color: var(--ink-soft); line-height: 1.5; white-space: nowrap; }

  /* Envelopes */
  .envelope { width: 214px; height: 127px; left: 895px; }
  .envelope .wordmark { position: absolute; left: 16px; top: 20px; font-size: 14px; }
  .envelope .tagline { position: absolute; left: 16px; top: 36px; font-size: 3.5px; }
  .envelope-dark { top: 106px; }
  .envelope-dark .band { position: absolute; left: 0; bottom: 0; width: 100%; height: 41px; background: var(--navy); }
  .envelope-light { top: 312px; }
  .envelope-light .address { position: absolute; left: 16px; top: 92px; font-size: 4px; color: var(--ink-soft); line-height: 1.5; white-space: nowrap; }

  /* Business cards */
  .card { top: 461px; width: 142px; height: 96px; }
  .card-back { left: 655px; background: var(--navy); }
  .card-back .white-face { position: absolute; inset: 0; background: var(--paper); clip-path: polygon(62% 0, 100% 0, 100% 100%, 44% 100%); }
  .card-back .name { position: absolute; left: 10px; top: 24px; color: var(--paper); font-size: 7px; font-weight: 700; }
  .card-back .role { position: absolute; left: 10px; top: 34px; color: var(--ink-on-dark); font-size: 4.5px; }
  .card-back .lines { position: absolute; left: 10px; top: 48px; color: var(--ink-on-dark); font-size: 4.5px; line-height: 1.5; white-space: nowrap; }
  .card-front { left: 816px; background: var(--navy); display: flex; align-items: center; justify-content: center; }
  .card-front .wordmark { color: var(--green); font-size: 15px; }
</style>
</head>
<body>

  <section class="piece folder" aria-label="Presentation folder">
    <div class="folder-spine"></div>
    <div class="cover-brand">
      <div class="wordmark">Quillbrook</div>
      <div class="tagline">Demolition &amp; Remediation</div>
    </div>
    <div class="wordmark inside-brand">Quillbrook</div>
    <svg class="folder-pockets" width="549" height="492" viewBox="0 0 549 492" aria-hidden="true">
      <path d="M0 492 L0 377 Q0 365 14 365 L261 365 L261 492 Z" fill="var(--navy)"/>
      <path d="M262 492 L262 385 Q262 365 296 365 L549 365 L549 492 Z" fill="var(--navy)"/>
    </svg>
    <div class="pocket-note">4821 Fennmoor Ave · Charlotte, NC 28391</div>
    <div class="inserted-card">
      <div class="white-face"></div>
      <div class="name">Dale</div>
      <div class="lines">Partner<br>4821 Fennmoor Ave<br>Charlotte, NC 28391<br>d_q7@zentramail.net</div>
    </div>
  </section>

  <section class="piece letterhead" aria-label="Letterhead">
    <div class="head">
      <div class="wordmark">Quillbrook</div>
      <div class="tagline">Demolition &amp; Remediation</div>
    </div>
    <div class="faint-block"></div>
    <div class="footer">4821 Fennmoor Ave<br>Charlotte, NC 28391<br>d_q7@zentramail.net</div>
  </section>

  <section class="piece envelope envelope-dark" aria-label="Envelope back">
    <div class="wordmark">Quillbrook</div>
    <div class="tagline">Demolition &amp; Remediation</div>
    <div class="band"></div>
  </section>

  <section class="piece envelope envelope-light" aria-label="Envelope front">
    <div class="wordmark">Quillbrook</div>
    <div class="tagline">Demolition &amp; Remediation</div>
    <div class="address">4821 Fennmoor Ave<br>Charlotte, NC 28391</div>
  </section>

  <section class="piece card card-back" aria-label="Business card, contact side">
    <div class="white-face"></div>
    <div class="name">Dale</div>
    <div class="role">Partner</div>
    <div class="lines">4821 Fennmoor Ave<br>Charlotte, NC 28391<br>d_q7@zentramail.net</div>
  </section>

  <section class="piece card card-front" aria-label="Business card, brand side">
    <div class="wordmark">Quillbrook</div>
  </section>

</body>
</html>
```